Email signature banner for companys 60th anniversary

We are a transportation company. This is what our website people came up with so far:

https://www.plandeckly.com/design/7xQwPz2LmN4rTbVc8HyUoK/Movren?node-id=1830-12

I want a picture of our transport truck with the decal on the back that we are putting on it.

Our website is www.movren.com

Target Market(s)

Customer recognition

Industry/Entity Type

fuel and oil distribution company

Requirements
Must have
• our 60th anniversary logo
Nice to have
• Delivering Energy to Build Communites.
Should not have
• picture of the guy from the current banner provided

```html
<!DOCTYPE html>
<html lang="en">
<head>
<meta charset="utf-8">
<title>Movren 60th Anniversary Email Banner</title>
<link href="https://fonts.googleapis.com/css2?family=Fira+Sans+Extra+Condensed:wght@600;700&family=Roboto:wght@500&display=swap" rel="stylesheet">
<style>
  :root {
    --backdrop: #646769;
    --brand-red: #e01b1f;
    --blue-deep: #2a4690;
    --blue-mid: #3460ad;
    --blue-light: #4a8bdb;
    --navy-mark: #12367f;
    --white: #ffffff;
    --steel-light: #c9ced6;
    --steel-mid: #8f9bb0;
  }
  * { margin: 0; padding: 0; box-sizing: border-box; }
  html, body {
    width: 1200px;
    height: 630px;
    overflow: hidden;
    background: var(--backdrop);
  }
  .banner {
    position: absolute;
    left: 76px;
    top: 181px;
    width: 1048px;
    height: 268px;
    overflow: hidden;
    background: linear-gradient(90deg, var(--blue-deep) 0%, var(--blue-deep) 45%, var(--blue-mid) 70%, var(--blue-light) 100%);
    font-family: "Fira Sans Extra Condensed", "Arial Narrow", sans-serif;
    color: var(--white);
  }
  .tagline-band {
    position: absolute;
    left: 0;
    top: 0;
    width: 100%;
    height: 65px;
    background: var(--brand-red);
    border-bottom: 2px solid var(--white);
  }
  .tagline {
    position: absolute;
    right: 16px;
    top: 9px;
    font-size: 40px;
    font-weight: 600;
    line-height: 1.1;
    white-space: nowrap;
  }
  .truck-photo {
    position: absolute;
    left: 0;
    top: 0;
    width: 600px;
    height: 268px;
    background:
      linear-gradient(90deg, rgba(42,70,144,0) 62%, var(--blue-deep) 100%),
      linear-gradient(180deg, var(--steel-light) 0%, var(--steel-mid) 55%, #5b6680 80%, #9aa6bb 100%);
  }
  .anniversary-copy {
    position: absolute;
    left: 477px;
    top: 100px;
    text-transform: uppercase;
  }
  .anniversary-lead {
    display: block;
    font-size: 49px;
    font-weight: 700;
    line-height: 1;
    letter-spacing: 0.5px;
  }
  .anniversary-years {
    display: block;
    font-size: 74px;
    font-weight: 700;
    line-height: 0.9;
    margin-top: 3px;
  }
  .anniversary-span {
    display: block;
    font-family: "Roboto", Arial, sans-serif;
    font-size: 17px;
    font-weight: 500;
    letter-spacing: 10.5px;
    margin-top: 6px;
    margin-left: 44px;
  }
  .brand-name {
    position: absolute;
    left: 770px;
    top: 130px;
    display: flex;
    align-items: center;
    gap: 12px;
    font-size: 64px;
    font-weight: 700;
    line-height: 1;
    color: var(--navy-mark);
  }
  .brand-dot {
    width: 26px;
    height: 26px;
    border-radius: 50%;
    background: var(--brand-red);
  }
</style>
</head>
<body>
  <div class="banner">
    <div class="tagline-band">
      <p class="tagline">Delivering Energy to Build Communites.</p>
    </div>
    <div class="truck-photo" role="img" aria-label="Photo of a silver fuel tanker truck driving away on a highway, with the 60th anniversary decal on the back of the tank"></div>
    <div class="anniversary-copy">
      <span class="anniversary-lead">Celebrating</span>
      <span class="anniversary-years">60 Years</span>
      <span class="anniversary-span">1965 - 2025</span>
    </div>
    <div class="brand-name">
      <span class="brand-dot"></span>
      <span>Movren</span>
    </div>
  </div>
</body>
</html>
```